Business Card for Kedrolin

I need a creative Business Card design for my start-up.
Kedrolin is a Vouchers (discounts) and media publisher, logo attached.
Info to be included:
First & Last name
Mobile Number
Email
Website
Social media accounts, Facebook, Insta, Linkedin.

```html
<!DOCTYPE html>
<html lang="en">
<head>
<meta charset="UTF-8">
<title>Kedrolin Business Card</title>
<link rel="stylesheet" href="https://fonts.googleapis.com/css2?family=Montserrat:wght@400;500;700;800&display=swap">
<style>
  :root {
    --navy: #25215f;
    --orange: #f7941d;
    --orange-deep: #e8701a;
    --white: #ffffff;
    --ink: #3a3a48;
    --stage: #2b2e34;
  }
  * { margin: 0; padding: 0; box-sizing: border-box; }
  html, body {
    width: 1200px; height: 900px; overflow: hidden;
    background: var(--stage);
    font-family: "Montserrat", sans-serif;
  }
  .canvas {
    position: relative; width: 1200px; height: 900px;
    display: flex; flex-direction: column; align-items: center; justify-content: center; gap: 44px;
  }
  .card {
    position: relative; width: 680px; height: 388px;
    border-radius: 22px; overflow: hidden;
  }
  .card-shapes { position: absolute; inset: 0; width: 100%; height: 100%; }

  /* Front */
  .card-front { background: var(--white); }
  .brand {
    position: absolute; left: 44px; top: 40px;
    display: flex; align-items: center; gap: 14px;
  }
  .brand-dot { width: 46px; height: 46px; border-radius: 50%; background: var(--orange); }
  .brand-name { font-weight: 800; font-size: 36px; color: var(--navy); letter-spacing: 0.5px; }
  .address {
    position: absolute; left: 46px; top: 128px;
    display: flex; gap: 10px; align-items: flex-start;
    font-size: 13px; line-height: 1.5; color: var(--ink);
  }
  .socials {
    position: absolute; left: 46px; top: 196px;
    list-style: none; font-size: 13px; color: var(--ink);
    display: flex; flex-direction: column; gap: 8px;
  }
  .socials li { display: flex; align-items: center; gap: 10px; }
  .social-dot { width: 12px; height: 12px; border-radius: 50%; background: var(--navy); flex: none; }
  .identity { position: absolute; right: 46px; top: 82px; text-align: right; }
  .person-name { font-weight: 800; font-size: 24px; color: var(--orange); letter-spacing: 0.5px; }
  .person-role { font-size: 14px; color: var(--ink); margin-top: 4px; }
  .contacts {
    position: absolute; left: 390px; top: 160px;
    list-style: none; font-size: 15px; color: var(--ink);
    display: flex; flex-direction: column; gap: 9px;
  }
  .contacts li { display: flex; align-items: center; gap: 10px; }
  .icon { width: 14px; height: 14px; flex: none; }

  /* Back */
  .card-back { background: var(--navy); }
  .back-brand {
    position: absolute; left: 0; right: 70px; top: 0; bottom: 0;
    display: flex; align-items: center; justify-content: center; gap: 18px;
  }
  .back-brand .brand-dot { width: 64px; height: 64px; }
  .back-brand .brand-name { color: var(--orange); font-size: 54px; }
</style>
</head>
<body>
<main class="canvas">

  <section class="card card-front" aria-label="Business card front">
    <svg class="card-shapes" viewBox="0 0 680 388" aria-hidden="true">
      <defs>
        <linearGradient id="orangeFade" x1="0" y1="0" x2="1" y2="1">
          <stop offset="0" stop-color="#f7941d"/>
          <stop offset="1" stop-color="#e8701a"/>
        </linearGradient>
      </defs>
      <!-- top edge: navy swoosh into orange band -->
      <path d="M210 0 H680 V12 H380 Q345 12 330 46 Q300 10 210 0Z" fill="var(--navy)"/>
      <path d="M330 46 Q345 12 385 12 H680 V46Z" fill="url(#orangeFade)"/>
      <!-- bottom edge: orange band into navy band -->
      <path d="M0 330 H270 Q305 332 320 388 H0Z" fill="url(#orangeFade)"/>
      <path d="M240 388 Q280 338 340 334 Q300 350 292 388Z" fill="url(#orangeFade)"/>
      <path d="M292 388 Q300 350 350 346 H680 V388Z" fill="var(--navy)"/>
    </svg>

    <div class="brand">
      <span class="brand-dot"></span>
      <span class="brand-name">Kedrolin</span>
    </div>

    <p class="address">
      <svg class="icon" viewBox="0 0 24 24" aria-hidden="true"><path d="M12 2a7 7 0 0 0-7 7c0 5 7 13 7 13s7-8 7-13a7 7 0 0 0-7-7zm0 9.5A2.5 2.5 0 1 1 12 6.5a2.5 2.5 0 0 1 0 5z" fill="var(--orange)"/></svg>
      <span>4120 Maple Ridge Lane<br>Dunmore, OR 97321</span>
    </p>

    <ul class="socials" aria-label="Social media accounts">
      <li><span class="social-dot"></span><span>/kedrolin</span></li>
      <li><span class="social-dot"></span><span>@kedrolin.media</span></li>
      <li><span class="social-dot"></span><span>/company/kedrolin</span></li>
    </ul>

    <div class="identity">
      <h1 class="person-name">MARCUS ELLERY</h1>
      <p class="person-role">CEO/Founder</p>
    </div>

    <ul class="contacts">
      <li>
        <svg class="icon" viewBox="0 0 24 24" aria-hidden="true"><path d="M6.6 10.8a15 15 0 0 0 6.6 6.6l2.2-2.2a1 1 0 0 1 1-.25 11.4 11.4 0 0 0 3.6.57 1 1 0 0 1 1 1V20a1 1 0 0 1-1 1A17 17 0 0 1 3 4a1 1 0 0 1 1-1h3.5a1 1 0 0 1 1 1c0 1.25.2 2.45.57 3.6a1 1 0 0 1-.25 1z" fill="var(--orange)"/></svg>
        <span>+44 000 318 7702</span>
      </li>
      <li>
        <svg class="icon" viewBox="0 0 24 24" aria-hidden="true"><rect x="2" y="5" width="20" height="14" rx="2" fill="var(--orange)"/><path d="M3 6l9 7 9-7" stroke="#fff" stroke-width="1.8" fill="none"/></svg>
        <span>hello@kedrolin.com</span>
      </li>
      <li>
        <svg class="icon" viewBox="0 0 24 24" aria-hidden="true"><circle cx="12" cy="12" r="10" fill="var(--orange)"/><path d="M2 12h20M12 2c3 3 3 17 0 20M12 2c-3 3-3 17 0 20" stroke="#fff" stroke-width="1.4" fill="none"/></svg>
        <span>www.kedrolin.com</span>
      </li>
    </ul>
  </section>

  <section class="card card-back" aria-label="Business card back">
    <svg class="card-shapes" viewBox="0 0 680 388" aria-hidden="true">
      <path d="M610 0 H680 V388 H610 Q585 388 585 360 V28 Q585 0 610 0Z" fill="var(--orange)"/>
    </svg>
    <div class="back-brand">
      <span class="brand-dot"></span>
      <span class="brand-name">Kedrolin</span>
    </div>
  </section>

</main>
</body>
</html>
```